Harlow Ironworks Business Card

We need a business card design for a new small metal fabrication business in rural NSW, Australia.

The business (Harlow Ironworks) is owner operated by a man with the initials KB - much of the branding comes from this name.

Harlow Ironworks designs, engineers, repairs and manufactures a range of custom, quality metal works including vehicle trays, agricultural machinery impliments, trailers, wood splitters, fire pits, furniture etc.

The brand position focuses on custom work of the highest quality.

Business card design should show quality, attention to detail and stand out among a mass of business cards.

Logos are in the files

The grey color may be changed on the logo if required to stand out more.

There is an image attached of a simple card that is liked because it is clean, clear, simple, masculine and effective. It says 'quality'. As most of the work we do is custom it would be good to have the business card speak to this.

Target Market(s)

Rural and regional based Australians. Primarily adult male 25-60 yrs. Primary production / rural / travelling lifestyle.

Industry/Entity Type

Metal Fabrication

Contact Information for Business Card

The words 'custom quality fabrications' would be great somewhere perhaps on the backside (not on the information side)
Name
title
Phone: 0418 539 746 and (02) 6193 4827
email: info@harlowiw.com.au
www.harlowiw.com.au

address (2 lines)

Requirements
Nice to have
• Background colour should be very navy blue or black.
Should not have
• NO orange and blue combinations.
• Navy is OK

```html
<!DOCTYPE html>
<html lang="en">
<head>
<meta charset="utf-8">
<title>Harlow Ironworks Business Card</title>
<link rel="stylesheet" href="https://fonts.googleapis.com/css2?family=Roboto+Condensed:wght@400;500&family=Nunito+Sans:wght@300;400;600&display=swap">
<style>
  :root {
    --green: #6cbe45;
    --grey-band: #a7a8ab;
    --grey-text: #8f9094;
    --card-light: #eeeeee;
    --card-edge: #e3e4e6;
    --white: #ffffff;
  }
  * { margin: 0; padding: 0; box-sizing: border-box; }
  html, body { width: 1200px; height: 1000px; overflow: hidden; background: var(--white); }
  body { position: relative; font-family: "Roboto Condensed", sans-serif; }

  .card-front { position: absolute; left: 83px; top: 83px; width: 621px; height: 383px; }
  .front-face {
    position: absolute; left: 0; top: 0; width: 621px; height: 336px;
    background: radial-gradient(ellipse 60% 62% at 50% 50%, #ffffff 0%, #f7f7f8 45%, var(--card-edge) 100%);
  }
  .social {
    position: absolute; right: 28px; top: 27px; display: flex; align-items: center; gap: 9px;
    color: var(--green); font-size: 15px; font-weight: 500;
  }
  .social-square { width: 22px; height: 22px; background: var(--green); border-radius: 3px; }
  .brand-name {
    position: absolute; left: 0; right: 0; top: 150px; text-align: center;
    font-family: "Roboto Condensed", sans-serif; font-weight: 500; font-size: 40px;
    letter-spacing: 3px; text-transform: uppercase; color: var(--grey-text);
  }
  .tagline-band {
    position: absolute; left: 0; top: 341px; width: 621px; height: 42px; background: var(--green);
    color: var(--white); text-align: center; font-size: 19px; font-weight: 500;
    letter-spacing: 2px; line-height: 36px;
  }

  .card-back { position: absolute; left: 505px; top: 535px; width: 624px; height: 385px; background: var(--card-light); }
  .person { position: absolute; left: 0; right: 0; top: 108px; text-align: center; }
  .person-name { font-family: "Nunito Sans", sans-serif; font-weight: 300; font-size: 38px; color: var(--green); letter-spacing: -0.5px; line-height: 1; }
  .person-name strong { font-weight: 400; }
  .person-title { font-family: "Nunito Sans", sans-serif; font-weight: 300; font-size: 17px; color: var(--grey-text); margin-top: 6px; }
  .contact-band {
    position: absolute; left: 0; top: 241px; width: 624px; height: 44px; background: var(--grey-band);
    display: flex; justify-content: center; align-items: center; gap: 26px; color: var(--white); font-size: 19px;
  }
  .web-band {
    position: absolute; left: 0; top: 290px; width: 624px; height: 44px; background: var(--green);
    display: flex; justify-content: center; align-items: center; gap: 6px; color: var(--white); font-size: 19px;
  }
  .contact-item { display: flex; align-items: center; gap: 8px; }
  .icon { display: block; }
</style>
</head>
<body>
  <section class="card-front">
    <div class="front-face">
      <div class="social"><span class="social-square"></span><span>HarlowIronworks</span></div>
      <div class="brand-name">Harlow Ironworks</div>
    </div>
    <div class="tagline-band">Custom quality fabrications</div>
  </section>

  <section class="card-back">
    <div class="person">
      <div class="person-name"><strong>Kieran</strong> Bowden</div>
      <div class="person-title">Director</div>
    </div>
    <div class="contact-band">
      <div class="contact-item">
        <svg class="icon" width="28" height="28" viewBox="0 0 28 28" aria-hidden="true">
          <circle cx="14" cy="14" r="12.5" fill="none" stroke="#fff" stroke-width="1.6"/>
          <path d="M9.5 8 l2.5 -0.5 l1.5 3.5 l-1.6 1.3 c0.8 1.8 2 3 3.8 3.8 l1.3 -1.6 l3.5 1.5 l-0.5 2.5 c-6 0.5 -11 -4.5 -10.5 -10.5z" fill="#fff"/>
        </svg>
        <span>0418 539 746 / (02) 6193 4827</span>
      </div>
      <div class="contact-item">
        <svg class="icon" width="28" height="28" viewBox="0 0 28 28" aria-hidden="true">
          <circle cx="14" cy="14" r="12.5" fill="none" stroke="#fff" stroke-width="1.6"/>
          <rect x="7.5" y="9.5" width="13" height="9" rx="1" fill="#fff"/>
          <path d="M7.5 10 l6.5 5 l6.5 -5" fill="none" stroke="#a7a8ab" stroke-width="1.2"/>
        </svg>
        <span>info@harlowiw.com.au</span>
      </div>
    </div>
    <div class="web-band">
      <svg class="icon" width="26" height="36" viewBox="0 0 26 36" aria-hidden="true">
        <path d="M2 2 L23 21 L14 21 L19 32 L15 34 L10 23 L2 29 Z" fill="none" stroke="#fff" stroke-width="1.6" stroke-linejoin="round"/>
      </svg>
      <span>www.harlowiw.com.au</span>
    </div>
  </section>
</body>
</html>
```